International Luxury Furniture and Accessories Outsourcing Company

We Need a Business Card design for a new Outsourcing company doing Business Internationally in the Luxury Furniture and Accessories Space. The company's name is GARETH VELLOR and we deal with clients in the high end and Luxury Space for Furniture and Accessories in the world. We would like Designs that speaks Luxury and Professionalism.

We like the Combination of the color Brown and Gold or Black and Gold. We are also open to other color combo.

We like some of the design of file attached.
Updates

This is Marcus and We really appreciate all of you taking the time out and putting the effort to help us jump start our new company. We have 2-3 designs that we like and will decide soon to pick one. Once again, Thank you to all of you !! Best Regards, Marcus

Industry/Entity Type

Business

```html
<!DOCTYPE html>
<html lang="en">
<head>
<meta charset="utf-8">
<title>Gareth Vellor – Business Card</title>
<link rel="stylesheet" href="https://fonts.googleapis.com/css2?family=Archivo+Narrow:wght@600&family=Oswald:wght@300&display=swap">
<style>
  :root {
    --backdrop: #3b2318;
    --gold-light: #f6f2c2;
    --gold-mid: #ece49c;
    --gold-deep: #d3c86a;
    --panel-light: #efebec;
    --panel-deep: #c8c1c4;
    --accent-green: #a3d162;
    --ink: #1c1a16;
    --detail-text: #fbfafa;
    --detail-shadow: rgba(90, 80, 85, 0.85);
    --card-shadow: rgba(0, 0, 0, 0.55);
  }
  * { margin: 0; padding: 0; box-sizing: border-box; }
  html, body {
    width: 1200px;
    height: 1000px;
    overflow: hidden;
    background: var(--backdrop);
  }
  .canvas {
    position: relative;
    width: 1200px;
    height: 1000px;
  }
  .card {
    position: absolute;
    left: 260px;
    width: 680px;
    height: 400px;
    overflow: hidden;
    box-shadow: 0 14px 30px var(--card-shadow);
  }
  .card--front {
    top: 70px;
    background: linear-gradient(172deg, var(--gold-light) 0%, var(--gold-mid) 55%, var(--gold-deep) 100%);
    display: flex;
    align-items: center;
    justify-content: center;
  }
  .brand-name {
    font-family: "Archivo Narrow", "Arial Narrow", sans-serif;
    font-weight: 600;
    color: var(--ink);
    letter-spacing: 0.02em;
  }
  .card--front .brand-name {
    font-size: 40px;
  }
  .card--back {
    top: 530px;
    display: flex;
  }
  .back-identity {
    width: 218px;
    height: 100%;
    background: linear-gradient(172deg, var(--gold-light) 0%, var(--gold-mid) 55%, var(--gold-deep) 100%);
    border-right: 6px solid var(--accent-green);
    display: flex;
    align-items: flex-end;
    justify-content: center;
    padding-bottom: 82px;
  }
  .back-identity .brand-name {
    font-size: 22px;
  }
  .back-details {
    flex: 1;
    background: linear-gradient(180deg, var(--panel-light) 0%, var(--panel-deep) 100%);
    position: relative;
  }
  .contact-list {
    position: absolute;
    right: 205px;
    top: 90px;
    list-style: none;
    text-align: right;
    font-family: "Oswald", "Arial Narrow", sans-serif;
    font-weight: 300;
    font-size: 25px;
    line-height: 1.12;
    color: var(--detail-text);
    text-shadow: 1px 2px 3px var(--detail-shadow);
  }
</style>
</head>
<body>
  <main class="canvas">
    <section class="card card--front" aria-label="Business card front">
      <h1 class="brand-name">GARETH VELLOR</h1>
    </section>

    <section class="card card--back" aria-label="Business card back">
      <div class="back-identity">
        <p class="brand-name">GARETH VELLOR</p>
      </div>
      <div class="back-details">
        <ul class="contact-list">
          <li>name</li>
          <li>position</li>
          <li>phone</li>
          <li>email</li>
          <li>website</li>
        </ul>
      </div>
    </section>
  </main>
</body>
</html>
```